organic, healthy living website needs a new home page!

We need a home page for the front page of our website (www.fernmeadowco.com.au).

We want to see the following at a glance! We want to gain trust - communicate value, and navigate visitors to the next step - purchasing!

Our two main products:
- certified organic veggies (weekly in Melbourne, Australia - Mentone, Frankston and Ringwood with more pick up locations to come soon)

-ethical wooden toys (by membership only at this stage - run quarterly as a bulk buy - just for Melbourne people!)

Other products:
- health appliances - juicers, dehydrators and water filters (free delivery to their door all over Australia)

- natural parenting products which promote breastfeeding, homebirth, cosleeping and gentle parenting (books, jewellery, gifts, blessingway etc) all over Australia - send via Southern Parcelway.

This website holds all of our products for purchase. We want to emphasise exactly what is to offer here. We will have an info blog which we want to link THROUGH the product homepage of FM. The blog will include a directory of natural services (for a very niche market), recipes, stories, and a wealth of information to do with natural pregnancy, health, parenting, health and community!

We have 5 images linked below - we need these to correspond with the words PREGNANCY, BIRTH, PARENTING, HEALTH, And COMMUNITY and maybe a little design on these - such as dragonflies or flowers - or both. We will code these to work in a slideshow, and link to our blog.

We want this page to feature everything we do, but also be aesthetically pleasing without overkill. We want it to reflect our style, and vision. Natural, organic, and as close to nature as possible. Flow is important, as is consistency throughout the page. WE want it to appeal to our hippy mamas and papas who just want to love their babies, live organically and as healthy as they can.

We love the look and feel of the following websites:

http://brightlarderhub.com/

Thank you!!

Target Market(s)

20-50 year old parents who are environmentally aware and health conscious. They have very close bonds to their children.
Think bohemian, rustic, vintage yet with a modern feel.

Industry/Entity Type

Health

Font styles to use
Script

Colors
e34197
6b449b
33a6d7
0455a3
33b7a4

Requirements
Must have
• Must be clean and say at a glance exactly what we do.

```html
<!DOCTYPE html>
<html lang="en">
<head>
<meta charset="utf-8">
<title>FernMeadow – Organic Living for Natural Families</title>
<link rel="stylesheet" href="https://fonts.googleapis.com/css2?family=Lobster&family=Courgette&family=Parisienne&family=Open+Sans:wght@400;600;700&family=Lora:wght@400;700&display=swap">
<style>
:root{
  --ink:#1f1d1f;
  --white:#ffffff;
  --purple:#6b449b;
  --pink:#e34197;
  --sky:#33a6d7;
  --teal:#33b7a4;
  --label-red:#c0202f;
  --text-grey:#555555;
  --peach-top:#fbe6d0;
  --peach-bottom:#fde9da;
  --card-dark:#1b1a1d;
}
*{box-sizing:border-box;margin:0;padding:0}
html,body{width:1200px;height:2182px;overflow:hidden;background:var(--white)}
.page{position:relative;width:1200px;height:2182px;overflow:hidden;font-family:"Open Sans",sans-serif}
.abs{position:absolute}

/* top utility bar */
.utility-bar{left:0;top:0;width:1200px;height:41px;background:var(--ink);color:var(--white);font-size:12px}
.utility-links{left:156px;top:12px;display:flex;gap:16px}
.utility-links span{display:flex;align-items:center;gap:5px}
.utility-links svg{width:11px;height:11px;fill:var(--white)}
.account-links{left:919px;top:11px;display:flex;align-items:center;gap:14px}
.account-links .divider{width:1px;height:18px;background:var(--teal)}

/* header */
.site-header{left:0;top:41px;width:1200px;height:138px;background:linear-gradient(var(--peach-top),var(--peach-bottom))}
.brand{left:0;width:1200px;top:22px;display:flex;justify-content:center;align-items:center;gap:10px}
.brand-mark{width:30px;height:30px;border-radius:50%;background:var(--purple)}
.brand-name{font-family:"Lora",serif;font-size:28px;color:var(--purple)}
.main-nav{left:0;width:1200px;top:103px;display:flex;justify-content:center;gap:28px;font-size:11px;color:var(--ink);text-transform:uppercase}
.main-nav .active{border-bottom:2px solid var(--pink);padding-bottom:6px}

/* hero slideshow (first slide) */
.hero{left:0;top:179px;width:1200px;height:410px;background:linear-gradient(180deg,#e9b781 0%,#d99a62 45%,#b9865f 70%,#c89a72 100%)}
.hero-title{left:0;width:1200px;top:392px;text-align:center;font-family:"Parisienne",cursive;font-size:86px;line-height:100px;color:var(--white)}
.shop-now{left:827px;top:522px;width:156px;height:40px;background:#111;color:var(--white);font-weight:700;font-size:19px;text-align:center;line-height:40px;font-style:italic;letter-spacing:.5px}

/* intro */
.intro{left:0;top:589px;width:1200px;height:352px;background:var(--purple);color:var(--white)}
.intro h1{position:absolute;top:22px;width:1200px;text-align:center;font-family:"Lobster",cursive;font-weight:400;font-size:36px}
.intro p{position:absolute;left:160px;top:90px;width:892px;font-family:"Courgette",cursive;font-size:13.4px;line-height:25.4px;text-align:justify}

/* hot deal products */
.section-title{left:0;width:1200px;text-align:center;font-family:"Lobster",cursive;font-weight:400;font-size:36px;line-height:50px;color:var(--ink)}
.product-card{top:1042px;width:203px;height:272px;background:var(--card-dark);border:1px solid #444}
.product-photo{position:absolute;left:0;top:0;width:201px;height:160px;background:radial-gradient(circle at 50% 45%,#3f6e9a 0%,#1b2a3a 45%,var(--card-dark) 75%)}
.product-name{position:absolute;top:160px;width:201px;text-align:center;font-family:"Parisienne",cursive;font-size:19px;line-height:30px;color:var(--white)}
.product-price{position:absolute;top:191px;width:201px;height:52px;background:var(--pink);color:var(--white);text-align:center;font-family:"Lora",serif;font-weight:700;font-size:36px;line-height:52px}
.product-rating{position:absolute;left:0;top:250px;width:201px;height:11px}

/* range highlights */
.highlights{left:0;top:1370px;width:1200px;height:384px;background:var(--sky)}
.highlights-title{position:absolute;top:22px;width:1200px;text-align:center;font-family:"Parisienne",cursive;font-weight:400;font-size:40px;line-height:54px;color:var(--white)}
.highlight{position:absolute;top:107px;width:277px}
.highlight-photo{position:relative;width:277px;height:156px;border:4px solid var(--white)}
.highlight-label{position:absolute;left:2px;top:102px;padding:0 9px;height:31px;line-height:31px;background:var(--label-red);color:var(--white);font-family:"Lobster",cursive;font-size:19px}
.highlight p{margin-top:22px;text-align:center;font-family:"Courgette",cursive;font-size:11.5px;line-height:17px;color:var(--white);padding:0 4px}

/* testimonials */
.testimonial-title{left:0;width:1200px;top:1786px;text-align:center;font-family:"Parisienne",cursive;font-weight:400;font-size:44px;line-height:58px;color:var(--ink)}
.person-photo{width:96px;border-radius:48px 48px 0 0;background:linear-gradient(#d9c4b4,#2c2c30 60%)}
.testimonial-text{width:230px}
.testimonial-text h3{font-family:"Lora",serif;font-weight:400;font-size:15px;color:var(--ink)}
.testimonial-text h4{font-family:"Lora",serif;font-weight:400;font-size:11px;color:var(--pink);margin-top:1px}
.testimonial-text p{font-family:"Lora",serif;font-size:11px;line-height:15px;color:var(--text-grey);margin-top:8px}

/* footer */
.footer-rule{left:0;top:2032px;width:1200px;height:9px;background:var(--teal)}
.site-footer{left:0;top:2041px;width:1200px;height:141px;background:var(--ink);color:var(--white)}
.footer-nav{position:absolute;top:30px;width:1200px;display:flex;justify-content:center;gap:32px;font-size:11px;text-transform:uppercase}
.copyright{position:absolute;top:92px;width:1200px;text-align:center;font-size:12px}
.social{position:absolute;top:65px;width:44px;height:44px;border-radius:50%}
</style>
</head>
<body>
<div class="page">

  <div class="abs utility-bar">
    <div class="abs utility-links">
      <span><svg viewBox="0 0 10 10"><path d="M5 1 1 5h1.5v4h2V6.5h1V9h2V5H9z"/></svg>Home</span>
      <span><svg viewBox="0 0 10 10"><circle cx="5" cy="3" r="2.2"/><path d="M1 10c0-3 2-4.5 4-4.5S9 7 9 10z"/></svg>My Account</span>
      <span><svg viewBox="0 0 10 10"><path d="M0 1h2l1.5 5h5L10 3H3" stroke="#fff" fill="none"/><circle cx="4" cy="8.5" r="1"/><circle cx="8" cy="8.5" r="1"/></svg>My Cart</span>
      <span><svg viewBox="0 0 10 10"><path d="M5 9 1 5a2.2 2.2 0 0 1 4-3 2.2 2.2 0 0 1 4 3z"/></svg>Wish List</span>
    </div>
    <div class="abs account-links"><span>Register</span><span class="divider"></span><span>Login</span></div>
  </div>

  <header class="abs site-header">
    <div class="abs brand"><span class="brand-mark"></span><span class="brand-name">FernMeadow</span></div>
    <nav class="abs main-nav">
      <span class="active">Home</span><span>Health Appliances</span><span>Natural Parenting</span><span>Blog</span>
    </nav>
  </header>

  <section class="abs hero" role="img" aria-label="Blog slideshow, Parenting slide: family of four walking hand in hand along a beach at sunset"></section>
  <div class="abs hero-title">Parenting</div>
  <div class="abs shop-now">SHOP NOW</div>

  <section class="abs intro">
    <h1>Organic Living, Delivered</h1>
    <p>Welcome to FernMeadow, your home for natural, organic and gentle family living. Every week we bring certified organic veggies to Melbourne families, with pick up in Mentone, Frankston and Ringwood and more locations coming soon. Our ethical wooden toys are offered by membership only, run quarterly as a bulk buy just for Melbourne families who want simple, lasting play. For the whole country we stock health appliances, from juicers and dehydrators to water filters, with free delivery to your door anywhere in Australia. Our natural parenting range supports breastfeeding, homebirth, cosleeping and gentle parenting, with books, jewellery, gifts and blessingway treasures sent Australia wide via Southern Parcelway. Visit our blog for a directory of natural services, wholesome recipes, real stories and a wealth of information on pregnancy, birth, parenting, health and community. Everything here is chosen with love for mamas, papas and little ones who want to live as close to nature as they can. Shop the range today and join our growing community.</p>
  </section>

  <h2 class="abs section-title" style="top:952px">Hot Deal</h2>

  <div class="abs product-card" style="left:173px">
    <div class="product-photo" role="img" aria-label="Red slow juicer on dark background"></div>
    <div class="product-name">Slow Juicer Red</div>
    <div class="product-price">$550</div>
    <svg class="product-rating" viewBox="0 0 201 11"><g fill="#fff"><path d="M80 .5l1.3 3.3 3.5.2-2.7 2.3.9 3.4L80 7.8l-3 1.9.9-3.4-2.7-2.3 3.5-.2z"/><path d="M90 .5l1.3 3.3 3.5.2-2.7 2.3.9 3.4L90 7.8l-3 1.9.9-3.4-2.7-2.3 3.5-.2z"/><path d="M100 .5l1.3 3.3 3.5.2-2.7 2.3.9 3.4-3-1.9-3 1.9.9-3.4-2.7-2.3 3.5-.2z"/><path d="M110 .5l1.3 3.3 3.5.2-2.7 2.3.9 3.4-3-1.9-3 1.9.9-3.4-2.7-2.3 3.5-.2z"/></g><path fill="#33a6d7" d="M120 .5l1.3 3.3 3.5.2-2.7 2.3.9 3.4-3-1.9-3 1.9.9-3.4-2.7-2.3 3.5-.2z"/></svg>
  </div>
  <div class="abs product-card" style="left:386px">
    <div class="product-photo" role="img" aria-label="Silver slow juicer on dark background"></div>
    <div class="product-name">Cold Press Juicer</div>
    <div class="product-price">$550</div>
    <svg class="product-rating" viewBox="0 0 201 11"><g fill="#fff"><path d="M80 .5l1.3 3.3 3.5.2-2.7 2.3.9 3.4L80 7.8l-3 1.9.9-3.4-2.7-2.3 3.5-.2z"/><path d="M90 .5l1.3 3.3 3.5.2-2.7 2.3.9 3.4L90 7.8l-3 1.9.9-3.4-2.7-2.3 3.5-.2z"/><path d="M100 .5l1.3 3.3 3.5.2-2.7 2.3.9 3.4-3-1.9-3 1.9.9-3.4-2.7-2.3 3.5-.2z"/><path d="M110 .5l1.3 3.3 3.5.2-2.7 2.3.9 3.4-3-1.9-3 1.9.9-3.4-2.7-2.3 3.5-.2z"/></g><path fill="#33a6d7" d="M120 .5l1.3 3.3 3.5.2-2.7 2.3.9 3.4-3-1.9-3 1.9.9-3.4-2.7-2.3 3.5-.2z"/></svg>
  </div>
  <div class="abs product-card" style="left:599px">
    <div class="product-photo" role="img" aria-label="Silver slow juicer on dark background"></div>
    <div class="product-name">Slow Juicer Silver</div>
    <div class="product-price">$550</div>
    <svg class="product-rating" viewBox="0 0 201 11"><g fill="#fff"><path d="M80 .5l1.3 3.3 3.5.2-2.7 2.3.9 3.4L80 7.8l-3 1.9.9-3.4-2.7-2.3 3.5-.2z"/><path d="M90 .5l1.3 3.3 3.5.2-2.7 2.3.9 3.4L90 7.8l-3 1.9.9-3.4-2.7-2.3 3.5-.2z"/><path d="M100 .5l1.3 3.3 3.5.2-2.7 2.3.9 3.4-3-1.9-3 1.9.9-3.4-2.7-2.3 3.5-.2z"/><path d="M110 .5l1.3 3.3 3.5.2-2.7 2.3.9 3.4-3-1.9-3 1.9.9-3.4-2.7-2.3 3.5-.2z"/></g><path fill="#33a6d7" d="M120 .5l1.3 3.3 3.5.2-2.7 2.3.9 3.4-3-1.9-3 1.9.9-3.4-2.7-2.3 3.5-.2z"/></svg>
  </div>
  <div class="abs product-card" style="left:812px">
    <div class="product-photo" role="img" aria-label="Silver slow juicer on dark background"></div>
    <div class="product-name">Whole Fruit Juicer</div>
    <div class="product-price">$550</div>
    <svg class="product-rating" viewBox="0 0 201 11"><g fill="#fff"><path d="M80 .5l1.3 3.3 3.5.2-2.7 2.3.9 3.4L80 7.8l-3 1.9.9-3.4-2.7-2.3 3.5-.2z"/><path d="M90 .5l1.3 3.3 3.5.2-2.7 2.3.9 3.4L90 7.8l-3 1.9.9-3.4-2.7-2.3 3.5-.2z"/><path d="M100 .5l1.3 3.3 3.5.2-2.7 2.3.9 3.4-3-1.9-3 1.9.9-3.4-2.7-2.3 3.5-.2z"/><path d="M110 .5l1.3 3.3 3.5.2-2.7 2.3.9 3.4-3-1.9-3 1.9.9-3.4-2.7-2.3 3.5-.2z"/></g><path fill="#33a6d7" d="M120 .5l1.3 3.3 3.5.2-2.7 2.3.9 3.4-3-1.9-3 1.9.9-3.4-2.7-2.3 3.5-.2z"/></svg>
  </div>

  <section class="abs highlights">
    <h2 class="highlights-title">What We Offer</h2>
    <div class="highlight" style="left:150px">
      <div class="highlight-photo" role="img" aria-label="Hands gathered around a smiley face drawn in flour" style="background:linear-gradient(135deg,#efe9e2,#cfc1b3)">
        <span class="highlight-label">Wooden Toys</span>
      </div>
      <p>Ethical wooden toys by membership, run quarterly as a bulk buy for Melbourne families only.</p>
    </div>
    <div class="highlight" style="left:458px">
      <div class="highlight-photo" role="img" aria-label="Sliced kiwi fruit halves" style="background:linear-gradient(135deg,#7fa640,#b9c98a 50%,#8a6f4d)">
        <span class="highlight-label">Organic Veggies</span>
      </div>
      <p>Certified organic veggies every week, pick up in Mentone, Frankston and Ringwood, more soon.</p>
    </div>
    <div class="highlight" style="left:768px">
      <div class="highlight-photo" role="img" aria-label="Hands resting on a pregnant belly with beaded bracelets" style="background:linear-gradient(135deg,#f2d7c8,#d8a98f)">
        <span class="highlight-label">Natural Parenting</span>
      </div>
      <p>Books, jewellery, gifts and blessingway treasures for gentle parenting, sent Australia wide.</p>
    </div>
  </section>

  <h2 class="abs testimonial-title">Testimonial</h2>
  <div class="abs person-photo" style="left:184px;top:1898px;height:134px" role="img" aria-label="Portrait of a smiling woman in a dark jacket"></div>
  <div class="abs testimonial-text" style="left:282px;top:1913px">
    <h3>Sarah Whitfield</h3>
    <h4>Veggie box member, Mentone</h4>
    <p>Our weekly veggie box is the highlight of our week. Fresh, organic and grown with real care.</p>
  </div>
  <div class="abs person-photo" style="left:690px;top:1892px;height:140px" role="img" aria-label="Portrait of a smiling man in a dark suit"></div>
  <div class="abs testimonial-text" style="left:812px;top:1913px">
    <h3>James Colby</h3>
    <h4>Toy club member, Ringwood</h4>
    <p>The wooden toys are beautiful and built to last. Our kids play with them every single day.</p>
  </div>

  <div class="abs footer-rule"></div>
  <footer class="abs site-footer">
    <nav class="footer-nav"><span>Home</span><span>Health Appliances</span><span>Natural Parenting</span><span>Blog</span></nav>
    <div class="copyright">Privacy / Copyright 2014</div>
    <span class="social" style="left:874px;background:#3b5998"></span>
    <span class="social" style="left:924px;background:#d34836"></span>
    <span class="social" style="left:974px;background:#3ba4e0"></span>
  </footer>

</div>
</body>
</html>
```